Aerospace Private Equity Firm Needs Website

We need a website for new private equity fund called Orlin Partners. We buy smaller companies in the aerospace and industrial industries. I have attached some information about the firm. An example of a site we like that is a similar business but focused in a different sector is www.travomedic.com. www.quarnestgrove.com is a firm that also invests in aerospace companies.

Industry/Entity Type

Equity

Number of Pages Required

1 page

Colors
0555a3
33a6d7
ec1f27

```html
<!DOCTYPE html>
<html lang="en">
<head>
<meta charset="utf-8">
<title>Orlin Partners</title>
<link rel="stylesheet" href="https://fonts.googleapis.com/css2?family=Questrial&family=Lato:wght@400;700&display=swap">
<style>
:root{
  --blue:#0555a3;
  --navy:#0b3a80;
  --sky:#33a6d7;
  --red:#ec1f27;
  --brick:#d12a2e;
  --rose:#d9585a;
  --mist:#f2f2f2;
  --ink:#333;
  --grey:#666;
  --char:#2d2d2d;
}
*{box-sizing:border-box;margin:0;padding:0}
html,body{width:1200px;height:3273px;overflow:hidden}
body{font-family:"Lato",sans-serif;color:var(--ink);background:#fff;position:relative}
h1,h2,h3{font-family:"Questrial",sans-serif;font-weight:400}
section,header,footer{position:relative;width:1200px;overflow:hidden}
ul{list-style:none}
a{color:inherit;text-decoration:none}

/* header */
.site-header{height:120px;background:var(--navy)}
.brand-panel{position:absolute;left:0;top:0;width:335px;height:120px;background:#e6eaf0;clip-path:polygon(0 0,100% 0,88% 100%,0 100%)}
.brand{position:absolute;left:80px;top:26px;font-family:"Questrial",sans-serif;color:var(--blue);font-size:44px;line-height:1}
.brand small{display:block;font-size:20px;margin-left:120px;margin-top:2px}
.social{position:absolute;display:flex;gap:10px}
.social span{width:30px;height:30px;border-radius:50%;background:var(--red);display:block}
.header-social{left:524px;top:12px}
.phone{position:absolute;right:56px;top:14px;color:#fff;font-weight:700;font-size:22px;display:flex;align-items:center;gap:10px}
.main-nav{position:absolute;left:336px;top:80px;display:flex;gap:22px;color:#fff;font-size:15px}

/* hero */
.hero{height:491px}
.hero-photo{position:absolute;inset:0;background:linear-gradient(180deg,#3d5f8f 0%,#c97a3a 30%,#f0a238 42%,#6f6f78 60%,#4a4d55 100%)}
.hero-copy{position:absolute;left:0;right:0;top:170px;text-align:center;color:#fff}
.hero-copy h1{font-size:58px;letter-spacing:1px;line-height:1}
.hero-copy p{font-size:20px;margin-top:6px}
.btn{display:inline-block;background:var(--brick);color:#fff;font-size:20px;padding:14px 34px;font-family:"Lato",sans-serif}
.hero-copy .btn{margin-top:14px}

/* sectors */
.sectors{height:273px}
.sector{position:absolute;top:0;height:273px;color:#fff;padding:28px 0 0}
.sector-commercial{left:0;width:620px;background:var(--brick);clip-path:polygon(0 0,100% 0,97% 100%,0 100%)}
.sector-military{left:600px;width:600px;background:var(--blue);clip-path:polygon(0 0,93% 0,100% 50%,93% 100%,0 100%)}
.sector h2{font-size:31px;display:flex;align-items:center;gap:16px}
.sector p{font-size:15px;line-height:1.5;margin-top:12px;width:450px}
.sector-commercial h2{margin-left:120px}.sector-commercial p{margin-left:115px}
.sector-military h2{margin-left:38px}.sector-military p{margin-left:38px}

/* about */
.about{height:392px}
.mark{display:inline-block;width:30px;height:30px;background:var(--red);margin-right:14px;vertical-align:middle}
.about h2{position:absolute;left:78px;top:50px;font-size:40px;color:#555}
.about p{position:absolute;left:78px;top:110px;width:640px;font-size:14px;line-height:1.6;color:var(--grey)}
.about .btn{position:absolute;left:78px;top:268px}
.about-photo{position:absolute;left:740px;top:50px;width:400px;height:280px;background:radial-gradient(ellipse at center,#8b8f78 0%,#c4c7bc 45%,#fff 72%)}

/* panels */
.duo{height:415px;background:var(--mist)}
.panel-red{position:absolute;top:0;height:100%;background:var(--rose);color:#fff}
.panel h2{font-size:34px;display:flex;align-items:center}
.strategy{left:0;width:600px;clip-path:polygon(0 0,100% 0,94% 100%,0 100%);padding:42px 0 0 78px}
.strategy-icon{margin:18px 0 0 160px}
.strategy p{font-size:15px;line-height:1.55;width:470px;margin-top:10px}
.strategy .more{text-decoration:underline;font-size:17px}
.criteria{position:absolute;left:620px;top:42px;color:var(--ink)}
.criteria h2{color:var(--navy)}
.arrow-list{margin-top:14px}
.arrow-list li{font-size:15.5px;color:var(--grey);line-height:1.35;margin-bottom:10px;padding-left:38px;position:relative}
.arrow-list li::before{content:"";position:absolute;left:0;top:4px;width:22px;height:12px;background:var(--red);clip-path:polygon(0 0,100% 50%,0 100%,30% 50%)}
.criteria .arrow-list li{margin-bottom:9px}
.timeline{position:absolute;left:78px;top:50px;width:470px}
.timeline h2{color:var(--navy)}
.timeline .arrow-list{margin-top:34px}
.timeline .arrow-list li{margin-bottom:28px}
.factors{left:600px;width:600px;clip-path:polygon(6% 0,100% 0,100% 100%,0 100%);padding:42px 0 0 78px}
.factors .arrow-list li{color:#fff;margin-bottom:12px;width:430px}
.factors .arrow-list li::before{background:#fff}

/* team */
.our-team{height:399px;background:var(--navy);color:#fff}
.our-team h2{text-align:center;font-size:34px;padding-top:50px}
.member{position:absolute;top:148px;display:flex;gap:22px}
.member-photo{width:176px;height:170px;background:linear-gradient(180deg,#dfe3e8,#b9c0c8);border:4px solid #fff}
.member h3{font-size:19px;margin-top:6px}
.member p{font-size:13.5px;line-height:1.55;width:260px;margin-top:12px}
.member a{display:block;text-decoration:underline;font-size:18px;margin-top:10px}
.member-one{left:92px}.member-two{left:640px}
.team-divider{position:absolute;left:600px;top:148px;width:1px;height:170px;background:rgba(255,255,255,.5)}

/* partners */
.partners{height:277px}
.partner{position:absolute;font-family:"Questrial",sans-serif;font-weight:400;font-size:21px;white-space:nowrap;line-height:1}
.partner::before{content:"";display:inline-block;width:13px;height:13px;background:currentColor;margin-right:8px;vertical-align:-1px}

/* footer */
.site-footer{height:360px;background:var(--char);color:#ddd}
.footer-brand{position:absolute;left:80px;top:50px;font-family:"Questrial",sans-serif;color:#fff;font-size:44px;line-height:1}
.footer-brand small{display:block;font-size:20px;margin-left:120px}
.footer-about{position:absolute;left:80px;top:152px;width:250px;font-size:13.5px;line-height:1.6}
.footer-rule{position:absolute;left:80px;top:240px;width:250px;height:1px;background:#777}
.footer-social{left:80px;top:262px}
.footer-social span{width:42px;height:42px;background:#fff}
.footer-social span:first-child{background:var(--red)}
.foot-col{position:absolute;top:50px}
.foot-col h3{color:var(--red);font-size:19px;text-transform:uppercase}
.foot-links{left:378px}
.foot-links li{font-size:13.5px;line-height:26px}
.foot-links h3{margin-bottom:14px}
.foot-contact{left:572px}
.foot-contact h3{margin-bottom:22px}
.foot-contact li{display:flex;gap:14px;font-size:13.5px;line-height:1.6;margin-bottom:26px;width:270px}
.foot-news{left:852px}
.news-grid{display:grid;grid-template-columns:124px 124px;gap:16px;margin-top:22px}
.news-grid div{height:104px;background:linear-gradient(135deg,#9bb3c8,#5b7391)}

/* subscribe */
.subscribe-bar{height:131px;background:var(--navy);color:#fff}
.subscribe{position:absolute;left:80px;top:34px;width:612px;height:58px;background:#fff;border-radius:29px;border:4px solid #fff;box-shadow:0 0 0 2px #c8c8c8;display:flex;align-items:center}
.subscribe label{color:#333;font-size:16px;margin-left:24px;flex:1;display:flex;align-items:center;gap:12px}
.subscribe .btn{border-radius:26px;background:var(--red);padding:14px 34px;font-size:18px}
.copyright{position:absolute;left:912px;top:38px;font-size:13.5px;line-height:1.9}
.copyright strong{margin-left:24px}
.copyright span{display:block;margin-left:36px}
</style>
</head>
<body>

<header class="site-header">
  <div class="brand-panel"></div>
  <div class="brand">Orlin<small>Partners</small></div>
  <div class="social header-social" aria-label="Social links"><span></span><span></span><span></span><span></span></div>
  <div class="phone">
    <svg width="20" height="20" viewBox="0 0 24 24"><path fill="#ec1f27" d="M6.6 10.8a15 15 0 0 0 6.6 6.6l2.2-2.2c.3-.3.7-.4 1-.2 1.1.4 2.3.6 3.6.6.6 0 1 .4 1 1V20c0 .6-.4 1-1 1A17 17 0 0 1 3 4c0-.6.4-1 1-1h3.5c.6 0 1 .4 1 1 0 1.3.2 2.5.6 3.6.1.3 0 .7-.2 1z"/></svg>
    1-800-555-0142
  </div>
  <nav class="main-nav">
    <a>Home</a><a>Firm Overview</a><a>Strategy</a><a>Investment Criteria</a><a>Performance</a><a>Team</a><a>Key Factors</a><a>Case Study</a><a>Contact</a>
  </nav>
</header>

<section class="hero">
  <div class="hero-photo" role="img" aria-label="Passenger jet parked at an airport gate under a sunset sky"></div>
  <div class="hero-copy">
    <h1>ORLIN PARTNERS</h1>
    <p>There are many variations of passages of Lorem Ipsum available.</p>
    <a class="btn">CONTACT US</a>
  </div>
</section>

<section class="sectors">
  <div class="sector sector-commercial">
    <h2><svg width="80" height="40" viewBox="0 0 80 40"><path fill="#fff" d="M4 18h56c8 0 14 2 14 4s-6 4-14 4H30L18 38h-8l6-12H8L2 32H0l3-10zM30 18 20 4h8l16 14z"/></svg>Commercial Aerospace</h2>
    <p>Orlin Partners (“Orlin”) is a Los Angeles, California-based private equity firm formed in 2016 by Principals from Westbrook Hill Associates (WHA). Orlin focuses on lower middle-market control investments in aerospace and industrial companies based in North America. The Orlin team has invested successfully in these sectors over a 10- year period while at WHA.</p>
  </div>
  <div class="sector sector-military">
    <h2><svg width="58" height="58" viewBox="0 0 58 58"><path fill="#fff" d="M48 4c3-3 7 1 4 4L40 20l6 28-4 4-10-22-10 10 1 8-3 3-4-8-8-4 3-3 8 1 10-10L7 17l4-4 28 6z"/></svg>Military Aerospace</h2>
    <p>Orlin Partners (“Orlin”) is a Los Angeles, California-based private equity firm formed in 2016 by Principals from Westbrook Hill Associates (WHA). Orlin focuses on lower middle-market control investments in aerospace and industrial companies based in North America. The Orlin team has invested successfully in these sectors over a 10- year period while at WHA.</p>
  </div>
</section>

<section class="about">
  <h2><span class="mark"></span>About Orlin Partners</h2>
  <p>Orlin Partners (“Orlin”) is a Los Angeles, California-based private equity firm formed in 2016 by Principals from Westbrook Hill Associates (WHA). Orlin focuses on lower middle-market control investments in aerospace and industrial companies based in North America. The Orlin team has invested successfully in these sectors over a 10- year period while at WHA. Orlin focuses on lower middle-market control investments in aerospace and industrial companies based in North America.</p>
  <a class="btn">READ MORE</a>
  <div class="about-photo" role="img" aria-label="Military helicopter in flight"></div>
</section>

<section class="duo">
  <div class="panel panel-red strategy">
    <h2><span class="mark" style="background:var(--red)"></span>STRATEGY</h2>
    <svg class="strategy-icon" width="84" height="84" viewBox="0 0 84 84"><circle cx="42" cy="42" r="38" fill="none" stroke="#0b3a80" stroke-width="5"/><path fill="#0b3a80" d="M62 20c2-2 5 1 3 3L55 33l4 20-3 3-8-15-8 8 1 6-2 2-3-6-6-3 2-2 6 1 8-8-15-8 3-3 20 4z"/></svg>
    <p>Orlin will invest undervalued aerospace and industrial companies. Areas of focus will include metallic structures,fluid conveyance, composite structures and surfacetreatment companies. Industrial investments will targetcompanies that share commo characteristics withaerospace; namely, engineering-drivenprecisio manufacturing with regulated qualitycontrols and product certificationrequirements.<br><a class="more">READ MORE</a></p>
  </div>
  <div class="panel criteria">
    <h2><span class="mark"></span>INVESTMENT CRITERIA</h2>
    <ul class="arrow-list">
      <li>Value focused</li>
      <li>Family or entrepreneur-owned / Corporate carve-outs</li>
      <li>EBITDA up to $10mm</li>
      <li>Enterprise Value $20-$100mm</li>
      <li>Deploy $10-$25mm equity per investment</li>
      <li>Profitable, stable, cash-flowing companies</li>
      <li>Opportunity for growth, strategic &amp; operational change</li>
      <li>Target 70% aerospace / 30% industrial</li>
    </ul>
  </div>
</section>

<section class="duo">
  <div class="panel timeline">
    <h2><span class="mark"></span>TEAM TIMELINE</h2>
    <ul class="arrow-list">
      <li>60 years of combined investing and operating experience</li>
      <li>Worked together for over 10 years completing over 30 platform and add-o investments</li>
      <li>Partners have led 14 platform investments, deploying $266mm generating 2.7x gross MOIC</li>
    </ul>
  </div>
  <div class="panel panel-red factors">
    <h2><span class="mark" style="background:var(--red)"></span>KEY FACTORS</h2>
    <ul class="arrow-list">
      <li>Aerospace is a large, growing global market that has historically outperformed the broad market index</li>
      <li>Preferred partner with OEMs – facilitates introductions to potential investments</li>
      <li>LMM underserved by PE firms and investment banks</li>
      <li>Souther California</li>
      <li>Opportunity for growth, strategic &amp; operational change</li>
      <li>Multi-year diversified backlogs at OEM's and long</li>
    </ul>
  </div>
</section>

<section class="our-team">
  <h2><span class="mark"></span>OUR TEAM</h2>
  <div class="member member-one">
    <div class="member-photo" role="img" aria-label="Portrait photo of a partner"></div>
    <div>
      <h3>Er Declan Farrow BDS NUI</h3>
      <p>Lorem Ipsum is simply dummy text of the printing and typesetting industry. Lorem Ipsum has been the industry's standard dummy text ever since the 1500s.</p>
      <a>READ MORE</a>
    </div>
  </div>
  <div class="team-divider"></div>
  <div class="member member-two">
    <div class="member-photo" role="img" aria-label="Portrait photo of a partner"></div>
    <div>
      <h3>Er Elena Castell BA</h3>
      <p>Lorem Ipsum is simply dummy text of the printing and typesetting industry. Lorem Ipsum has been the industry's standard dummy text ever since the 1500s.</p>
      <a>READ MORE</a>
    </div>
  </div>
</section>

<section class="partners" aria-label="Portfolio companies">
  <span class="partner" style="left:180px;top:36px;color:#c62828">Borewell</span>
  <span class="partner" style="left:480px;top:36px;color:#333">Kestrel Works</span>
  <span class="partner" style="left:790px;top:36px;color:#0b3a80">Tallis Aero</span>
  <span class="partner" style="left:370px;top:114px;color:#0b3a80">Ferrum Finishing</span>
  <span class="partner" style="left:604px;top:114px;color:#333">Northgate Avionics</span>
  <span class="partner" style="left:906px;top:114px;color:#a8232a">Vermara</span>
  <span class="partner" style="left:86px;top:196px;color:#c62828">Plexon</span>
  <span class="partner" style="left:260px;top:196px;color:#0b3a80">Tandem Systems</span>
  <span class="partner" style="left:490px;top:196px;color:#0555a3">Coastline Aero</span>
</section>

<footer class="site-footer">
  <div class="footer-brand">Orlin<small>Partners</small></div>
  <p class="footer-about">Lorem Ipsum is simply dummy text of the printing and typeing Lorem Ipsum is simply dummy text of the printing and typeing</p>
  <div class="footer-rule"></div>
  <div class="social footer-social" aria-label="Social links"><span></span><span></span><span></span><span></span></div>

  <div class="foot-col foot-links">
    <h3>Useful Links</h3>
    <ul><li>Home</li><li>Firm Overview</li><li>Strategy</li><li>Investment Criteria</li><li>Performance</li><li>Team</li><li>Key Factors</li><li>Case Study</li><li>Contact</li></ul>
  </div>

  <div class="foot-col foot-contact">
    <h3>Contact Us</h3>
    <ul>
      <li><svg width="18" height="24" viewBox="0 0 18 24"><path fill="#ec1f27" d="M9 0a9 9 0 0 1 9 9c0 6-9 15-9 15S0 15 0 9a9 9 0 0 1 9-9zm0 5a4 4 0 1 0 0 8 4 4 0 0 0 0-8z"/></svg>4820 Harbor View Ave. Suite 210 Los Angeles, CA 90071</li>
      <li><svg width="18" height="18" viewBox="0 0 24 24"><path fill="#ec1f27" d="M6.6 10.8a15 15 0 0 0 6.6 6.6l2.2-2.2c.3-.3.7-.4 1-.2 1.1.4 2.3.6 3.6.6.6 0 1 .4 1 1V20c0 .6-.4 1-1 1A17 17 0 0 1 3 4c0-.6.4-1 1-1h3.5c.6 0 1 .4 1 1 0 1.3.2 2.5.6 3.6.1.3 0 .7-.2 1z"/></svg>(310) 555-0190</li>
      <li><svg width="18" height="18" viewBox="0 0 24 24"><rect x="2" y="2" width="20" height="20" rx="3" fill="none" stroke="#ec1f27" stroke-width="2.5"/><path d="M7 8h10M7 12h10M7 16h6" stroke="#ec1f27" stroke-width="2"/></svg>(310) 555-0190</li>
      <li><svg width="20" height="16" viewBox="0 0 20 16"><rect width="20" height="16" rx="2" fill="#ec1f27"/><path d="M1 2l9 7 9-7" fill="none" stroke="#2d2d2d" stroke-width="1.6"/></svg>support@orlinpartners.com</li>
    </ul>
  </div>

  <div class="foot-col foot-news">
    <h3>Latest News</h3>
    <div class="news-grid">
      <div role="img" aria-label="News photo: aircraft engineering"></div>
      <div role="img" aria-label="News photo: aircraft on the apron"></div>
      <div role="img" aria-label="News photo: aircraft interior"></div>
      <div role="img" aria-label="News photo: jet at the terminal"></div>
    </div>
  </div>
</footer>

<section class="subscribe-bar">
  <form class="subscribe">
    <label><svg width="22" height="16" viewBox="0 0 22 16"><rect x="1" y="1" width="20" height="14" rx="2" fill="none" stroke="#333" stroke-width="2"/><path d="M2 2l9 7 9-7" fill="none" stroke="#333" stroke-width="2"/></svg>Email</label>
    <a class="btn">SUBSCRIBE!</a>
  </form>
  <p class="copyright">©<strong>ORLIN PARTNERS</strong><span>2017 - All Rights Reserved</span></p>
</section>

</body>
</html>
```